Banner Ad

We need a banner ad for a service. The service is called, "PipeRook" It compiles tweets and Chatterloom posts about state government issues that are posted by U.S. State Legislators. We have a word cloud containing the issues we want to highlight. And we a logo for PipeRook.

The tag is:
Question: Who Is Talking About Issues on Social Media?
Answer: State Legislators
Are you Listening?

The banner ad will be used for print and web. It will go into a regular weekly publication called The Regional Ledger Roundup. http://www.civicpanel-example.com/the-regional-ledger-roundup/

Industry/Entity Type

Government

```html
<!DOCTYPE html>
<html lang="en">
<head>
<meta charset="utf-8">
<title>PipeRook — Who Is Talking About Issues on Social Media?</title>
<link href="https://fonts.googleapis.com/css2?family=Anton&family=Oswald:wght@400;500;600&display=swap" rel="stylesheet">
<style>
  :root {
    --navy-light: #1f5696;
    --navy: #1a4178;
    --navy-deep: #15305e;
    --white: #ffffff;
    --band-dark: #9c1734;
    --band-light: #b51f3f;
    --pink: #ee5a6f;
    --sky: #5cc8f2;
    --land: #e9e9ec;
    --word-blue: #1b5497;
    --word-red: #a71c3a;
    --word-black: #1a1a1a;
    --social-blue: #1766b0;
    --social-sky: #2aa6e0;
  }
  * { margin: 0; padding: 0; box-sizing: border-box; }
  html, body { width: 927px; height: 1200px; overflow: hidden; background: var(--navy-deep); }
  .ad {
    position: relative;
    width: 927px;
    height: 1200px;
    overflow: hidden;
    background: radial-gradient(ellipse at 50% 35%, var(--navy-light) 0%, var(--navy) 50%, var(--navy-deep) 100%);
    font-family: "Oswald", sans-serif;
    color: var(--white);
  }

  .brand {
    position: absolute;
    top: 92px; left: 0; width: 100%;
    display: flex; justify-content: center; align-items: center; gap: 12px;
  }
  .brand__dot { width: 36px; height: 36px; border-radius: 50%; background: var(--white); }
  .brand__name { font-family: "Oswald", sans-serif; font-weight: 500; font-size: 36px; letter-spacing: 2px; line-height: 1.2; color: var(--white); }

  .bubble {
    position: absolute;
    display: flex; align-items: center; justify-content: center;
    font-family: "Anton", sans-serif;
    font-size: 40px;
    color: var(--white);
  }
  .bubble--q { left: 68px; top: 256px; width: 110px; height: 100px; }
  .bubble--a { left: 672px; top: 222px; width: 118px; height: 104px; }
  .bubble svg { position: absolute; inset: 0; }
  .bubble span { position: relative; }

  .question {
    position: absolute;
    right: 496px; top: 231px;
    text-align: right;
    font-family: "Oswald", sans-serif;
    font-weight: 500;
    font-size: 45px;
    line-height: 72px;
    letter-spacing: -0.5px;
    white-space: nowrap;
  }

  .divider { position: absolute; width: 2px; background: rgba(255,255,255,0.75); }
  .divider--top { left: 463px; top: 207px; height: 256px; }
  .divider--foot { left: 463px; top: 1080px; height: 120px; }

  .answer { position: absolute; left: 0; top: 0; }
  .answer__line {
    position: absolute;
    left: 493px;
    font-family: "Anton", sans-serif;
    line-height: 1;
    white-space: nowrap;
    transform-origin: top left;
  }
  .answer__line--first { top: 228px; font-size: 72px; transform: scaleY(1.28); }
  .answer__line--second { top: 344px; font-size: 63px; transform: scaleY(1.4); }

  .band { position: absolute; left: 0; top: 0; }

  .map {
    position: absolute;
    left: 196px; top: 515px;
    width: 556px; height: 356px;
    background: var(--land);
    border-radius: 40px 60px 90px 70px / 40px 50px 120px 110px;
  }

  .cloud { position: absolute; inset: 0; }
  .word {
    position: absolute;
    font-family: "Oswald", sans-serif;
    font-weight: 500;
    line-height: 1;
    white-space: nowrap;
    letter-spacing: -0.5px;
  }
  .word--blue { color: var(--word-blue); }
  .word--red { color: var(--word-red); }
  .word--black { color: var(--word-black); }

  .pin { position: absolute; border-radius: 50%; }
  .pin--blue { background: var(--social-blue); }
  .pin--sky { background: var(--social-sky); }

  .network {
    position: absolute;
    width: 88px; height: 88px;
    border-radius: 50%;
    display: flex; align-items: center; justify-content: center;
    font-family: "Oswald", sans-serif; font-weight: 500;
    font-size: 14px; color: var(--white);
    box-shadow: 0 3px 8px rgba(0,0,0,0.3);
  }
  .network--chatterloom { left: 163px; top: 679px; background: var(--social-blue); }
  .network--chirpwire { left: 659px; top: 703px; background: var(--social-sky); }

  .listening {
    position: absolute;
    top: 917px; left: 0; width: 100%;
    text-align: center;
    font-family: "Oswald", sans-serif; font-weight: 500;
    font-size: 48px;
    letter-spacing: -0.5px;
  }

  .agency {
    position: absolute;
    left: 222px; top: 1090px;
    font-family: "Oswald", sans-serif; font-weight: 500;
    font-size: 23px; line-height: 1.2; letter-spacing: 0.3px;
    color: var(--white);
  }
  .contact {
    position: absolute;
    left: 494px; top: 1072px;
    font-family: "Oswald", sans-serif; font-weight: 400;
    font-size: 25px; line-height: 33px;
    color: var(--white);
  }
</style>
</head>
<body>
<main class="ad">

  <header class="brand">
    <span class="brand__dot"></span>
    <span class="brand__name">PipeRook</span>
  </header>

  <div class="bubble bubble--q">
    <svg viewBox="0 0 110 100" width="110" height="100" aria-hidden="true">
      <path d="M55 6 C84 6 104 24 104 48 C104 62 98 72 90 79 L102 94 L76 86 C70 88 62 90 55 90 C26 90 6 72 6 48 C6 24 26 6 55 6 Z" fill="var(--pink)"/>
    </svg>
    <span>Q</span>
  </div>

  <h1 class="question">Who Is Talking<br>About&nbsp; Issues<br>on Social Media?</h1>

  <div class="divider divider--top"></div>

  <p class="answer">
    <span class="answer__line answer__line--first">State</span>
    <span class="answer__line answer__line--second">Legislators</span>
  </p>

  <div class="bubble bubble--a">
    <svg viewBox="0 0 118 104" width="118" height="104" aria-hidden="true">
      <path d="M60 6 C90 6 112 25 112 50 C112 75 90 92 60 92 C50 92 42 90 34 86 L8 96 L20 78 C12 70 8 61 8 50 C8 25 30 6 60 6 Z" fill="var(--sky)"/>
    </svg>
    <span>A</span>
  </div>

  <svg class="band" width="927" height="1200" viewBox="0 0 927 1200" aria-hidden="true">
    <polygon points="0,685 927,445 927,545 0,794" fill="var(--band-dark)"/>
    <polygon points="0,794 927,545 927,665 0,905" fill="var(--band-light)"/>
  </svg>

  <div class="map" role="img" aria-label="Outline map of the United States in light grey, carrying the issue word cloud"></div>

  <div class="cloud">
    <span class="pin pin--sky" style="left:294px;top:524px;width:20px;height:20px"></span>
    <span class="pin pin--blue" style="left:191px;top:547px;width:22px;height:22px"></span>
    <span class="pin pin--sky" style="left:602px;top:596px;width:22px;height:22px"></span>
    <span class="pin pin--sky" style="left:701px;top:574px;width:34px;height:34px"></span>
    <span class="pin pin--blue" style="left:283px;top:798px;width:22px;height:22px"></span>
    <span class="pin pin--blue" style="left:349px;top:824px;width:32px;height:32px"></span>

    <span class="word word--blue" style="left:224px;top:527px;font-size:14px">FairShare</span>
    <span class="word word--red" style="left:280px;top:555px;font-size:18px">SharingEconomy</span>
    <span class="word word--red" style="left:436px;top:564px;font-size:21px">Drones</span>
    <span class="word word--blue" style="left:200px;top:580px;font-size:55px">MinimumWage</span>
    <span class="word word--black" style="left:514px;top:613px;font-size:33px">E-Cigs</span>
    <span class="word word--red" style="left:654px;top:619px;font-size:22px">GMO</span>
    <span class="word word--red" style="left:491px;top:645px;font-size:40px">CommonCore</span>
    <span class="word word--black" style="left:204px;top:652px;font-size:16.5px">DistractedDriving</span>
    <span class="word word--black" style="left:327px;top:651px;font-size:18px">AlternativeEnergy</span>
    <span class="word word--blue" style="left:262px;top:685px;font-size:42px">ClimateChange</span>
    <span class="word word--blue" style="left:523px;top:708px;font-size:26.5px">Immigration</span>
    <span class="word word--black" style="left:267px;top:744px;font-size:28px">Fracking</span>
    <span class="word word--black" style="left:360px;top:743px;font-size:53.5px">Transportation</span>
    <span class="word word--blue" style="left:204px;top:775px;font-size:15.5px">Bankruptcy</span>
    <span class="word word--red" style="left:213px;top:800px;font-size:16px">Privacy</span>
    <span class="word word--blue" style="left:398px;top:825px;font-size:16px">TaxReform</span>
  </div>

  <div class="network network--chatterloom">Chatterloom</div>
  <div class="network network--chirpwire">Chirpwire</div>

  <p class="listening">Are You Listening?</p>

  <div class="divider divider--foot"></div>

  <p class="agency">Civic Panel Associates</p>
  <p class="contact">Find out more details at<br>www.civicpanel-example.com</p>

</main>
</body>
</html>
```